Digital Mapping company needs a Proposal Cover Page template (Not Cover Letter).

We are looking for a new design of our proposal's front page. Sales people at Brindle Survey will use this new cover page when bidding for jobs, there will be Brindle Survey elements that will be set in stone but the potential client information will need to be adaptable/customizable (for example, we currently upload client logos to the home page of our proposals). I attach what we currently have.
Similar look and feel as our tradeshow booth pull up banners and website (www.brindlesurvey.example) (images of these are also attached). We would like to see designs that use similar colours: green/blue/teal/yellow/orange/red.

We have clients all over the world. We own state of the art mapping equipment (LiDAR). LiDAR and digital photography are acquired with our own Halvern 314 and other aircraft. The final proposal design should be recognizable and communicate: an experienced company, high quality, and state of the art mapping technology delivered worldwide.

Target Market(s)

Our clients are global and range from small business to large corporations. We have clients associated with Mining, Forestry, Engineering, Ecological and First Nations sectors (usually hired by Geologists & Engineers)

Industry/Entity Type

Technical Service

Font styles to use
Serif

Colors

Designer to choose colors to be used in the design.

Requirements
Must have
• Here are the basic items we would like to see on the cover page of our proposal:
• Our Company Name - Brindle Survey Ltd.
• Our Company Logo - attached
• Our Company contact information [customizable field as we have a few locations]
• Proposal service [customizable field to add]
• Proposal project name and location [customizable field to add]
• Proposal Job number [customizable field to add]
• Recipient company or individual and their logo [customizable field’s to add these]
• Date created [auto date]
• Subdued information/less focus on Brindle Survey’s name and contact information and a greater focus on the client and their project. Well chosen imagery will tie Brindle Survey’s services to the client’s needs without the client thinking about it. Good use of white space as well.
Nice to have
• Similar look and feel as our tradeshow booth pull up banners and website (images of these are attached). We would like to see designs that use similar colours: green/yellow/red/blue/teal.
Should not have
• Something that doesn't match or fit with our logo/website/pull up tradeshow banners that are attached. Something that doesn't include all the elements in our must have list.

```html
<!DOCTYPE html>
<html lang="en">
<head>
<meta charset="utf-8">
<title>Brindle Survey – Proposal Template</title>
<link href="https://fonts.googleapis.com/css2?family=Arimo:wght@400;700&family=Open+Sans:wght@600&display=swap" rel="stylesheet">
<style>
  :root {
    --backdrop: #3a3a3a;
    --navy: #1c3c66;
    --navy-deep: #163457;
    --navy-light: #2b5282;
    --white: #ffffff;
    --paper-grey: #f4f4f4;
    --body-grey: #8a8a8a;
    --contact-grey: #7a7a7a;
    --footer-grey: #5b5b5b;
    --footer-text: #b4b4b4;
    --placeholder-grey: #c2c2c2;
    --teal: #2f8fc0;
  }
  * { box-sizing: border-box; margin: 0; padding: 0; }
  html, body { width: 1200px; height: 960px; overflow: hidden; }
  body {
    background: var(--backdrop);
    font-family: "Arimo", Arial, sans-serif;
    position: relative;
  }
  .page {
    position: absolute;
    width: 470px;
    height: 608px;
    background: var(--white);
    display: flex;
    flex-direction: column;
    box-shadow: 0 10px 24px rgba(0,0,0,.45);
  }
  .page--cover { left: 81px; top: 176px; }
  .page--inner { left: 636px; top: 177px; }

  .top-band { height: 18px; background: var(--navy); flex: none; }

  .letterhead {
    height: 64px; flex: none;
    display: flex; justify-content: space-between; align-items: center;
    padding: 0 34px 0 35px;
    background: var(--white);
    position: relative; z-index: 1;
  }
  .page--inner .letterhead { height: 66px; box-shadow: 0 2px 3px rgba(0,0,0,.12); }
  .brand { display: flex; align-items: center; gap: 7px; }
  .brand__dot { width: 26px; height: 26px; border-radius: 50%; background: var(--teal); }
  .brand__name { font-weight: 700; font-size: 17px; color: var(--navy-deep); letter-spacing: .2px; }
  .contact { font-size: 7.4px; line-height: 9px; color: var(--contact-grey); width: 132px; }
  .contact__name { font-weight: 700; font-size: 8.5px; color: var(--navy); margin-bottom: 2px; }

  /* Cover hero */
  .hero {
    height: 184px; flex: none; position: relative;
    background: linear-gradient(180deg, var(--navy) 0%, var(--navy-deep) 100%);
    overflow: hidden;
  }
  .hero__art { position: absolute; inset: 0; }
  .hero__title { position: absolute; left: 49px; top: 36px; color: var(--white); font-weight: 700; font-size: 15px; }
  .hero__lede { position: absolute; left: 49px; top: 66px; width: 220px; color: var(--white); font-size: 10px; line-height: 13.5px; }
  .job-tag {
    position: absolute; left: 49px; top: 127px; width: 106px; height: 25px;
    border: 1.5px solid var(--white); border-radius: 4px;
    display: flex; align-items: center; justify-content: center;
    color: var(--white); font-family: "Open Sans", Arial, sans-serif; font-weight: 600; font-size: 9px;
  }

  .intro { height: 146px; flex: none; background: var(--paper-grey); padding: 15px 50px 0 50px; }
  .intro p { font-size: 8.7px; line-height: 11.5px; color: var(--body-grey); margin-bottom: 6px; }

  .client-logo { flex: 1; display: flex; align-items: center; justify-content: center; gap: 14px; }
  .client-logo__mark { width: 64px; height: 64px; background: var(--placeholder-grey); }
  .client-logo__name { font-weight: 700; font-size: 27px; line-height: 30px; color: var(--placeholder-grey); }

  /* Inner page */
  .section { padding: 0 66px; }
  .section h2 { font-size: 16px; font-weight: 700; color: var(--navy); margin-bottom: 7px; }
  .section p { font-size: 8.7px; line-height: 12.2px; color: var(--body-grey); }
  .section--toc { padding-top: 21px; height: 203px; flex: none; }
  .divider-band { height: 38px; flex: none; }
  .section--scope { padding-top: 28px; flex: 1; }

  .footer {
    height: 57px; flex: none; background: var(--footer-grey);
    display: flex; align-items: center;
    font-size: 8px; color: var(--footer-text);
  }
  .footer span { position: absolute; }
  .footer b { font-weight: 700; }
  .footer__cell { flex: 1; text-align: center; }
</style>
</head>
<body>

<section class="page page--cover">
  <div class="top-band"></div>
  <header class="letterhead">
    <div class="brand"><span class="brand__dot"></span><span class="brand__name">Brindle Survey</span></div>
    <address class="contact" style="font-style:normal">
      <div class="contact__name">Brindle Survey Ltd.</div>
      Unit 4, 880 Harbour Road<br>
      Fernvale BC, V0N 2K4, Canada<br>
      O. +1(555) 014-2280<br>
      info@brindlesurvey.example
    </address>
  </header>

  <div class="hero">
    <svg class="hero__art" width="470" height="184" viewBox="0 0 470 184">
      <defs>
        <linearGradient id="terrainFade" x1="0" y1="0" x2="0" y2="1">
          <stop offset="0" stop-color="#2b5282" stop-opacity=".15"/>
          <stop offset="1" stop-color="#2b5282" stop-opacity=".65"/>
        </linearGradient>
        <radialGradient id="aircraftGlow" cx=".5" cy=".4" r=".6">
          <stop offset="0" stop-color="#8ea6c6" stop-opacity=".5"/>
          <stop offset="1" stop-color="#8ea6c6" stop-opacity="0"/>
        </radialGradient>
      </defs>
      <path role="img" aria-label="Wireframe terrain surface" d="M0 103 Q120 112 240 100 T470 104 V184 H0 Z" fill="url(#terrainFade)"/>
      <rect role="img" aria-label="Survey aircraft scanning the terrain below" x="290" y="18" width="120" height="150" fill="url(#aircraftGlow)"/>
    </svg>
    <div class="hero__title">Brindle Survey Ltd.</div>
    <p class="hero__lede">Proposal to (Service we are providing) in (Project Location) for (Company Name).</p>
    <div class="job-tag">Job Number</div>
  </div>

  <div class="intro">
    <p>Lorem ipsum dolor sit amet, consectetur adipiscing elit, sed do eiusmod tempor incididunt ut labore et dolore magna aliqua. Ut enim ad minim veniam, quis nostrud exercitation ullamco laboris nisi ut aliquip ex ea commodo consequat. Duis aute irure dolor in reprehenderit in voluptate velit esse cillum dolore eu fugiat nulla pariatur. Excepteur sint occaecat cupidatat non proident, sunt in culpa qui officia deserunt mollit anim id est laborum.</p>
    <p>Lorem ipsum dolor sit amet, consectetur adipiscing elit, sed do eiusmod tempor incididunt ut labore et dolore magna aliqua. Ut enim ad minim veniam, quis nostrud exercitation ullamco laboris nisi ut aliquip ex ea commodo consequat. Duis aute pariatur.</p>
  </div>

  <div class="client-logo">
    <span class="client-logo__mark"></span>
    <span class="client-logo__name">Logo<br>Company</span>
  </div>

  <footer class="footer">
    <div class="footer__cell">Page <b>1</b> of <b>2</b></div>
    <div class="footer__cell">Confidential</div>
    <div class="footer__cell">Job Number</div>
  </footer>
</section>

<section class="page page--inner">
  <div class="top-band"></div>
  <header class="letterhead">
    <div class="brand"><span class="brand__dot"></span><span class="brand__name">Brindle Survey</span></div>
    <address class="contact" style="font-style:normal">
      <div class="contact__name">Brindle Survey Ltd.</div>
      Unit 4, 880 Harbour Road<br>
      Fernvale BC, V0N 2K4, Canada<br>
      O. +1(555) 014-2280<br>
      info@brindlesurvey.example
    </address>
  </header>

  <div class="section section--toc">
    <h2>Table of Contents</h2>
    <p>Sed ut perspiciatis unde omnis iste natus error sit voluptatem accusantium doloremque laudantium, totam rem aperiam, eaque ipsa quae ab illo inventore veritatis et quasi architecto beatae vitae dicta sunt explicabo. Nemo enim ipsam voluptatem quia voluptas sit aspernatur aut odit aut fugit, sed quia consequuntur magni dolores eos qui ratione voluptatem sequi nesciunt. Neque porro quisquam est, qui dolorem ipsum quia dolor sit amet, consectetur, adipisci velit, sed quia non numquam eius modi tempora incidunt ut labore et dolore magnam aliquam quaerat voluptatem. Ut enim ad minima veniam, quis nostrum exercitationem ullam corporis suscipit laboriosam, nisi ut aliquid ex ea commodi consequatur? Quis autem vel eum iure reprehenderit qui in ea voluptate velit esse quam nihil molestiae consequatur, vel illum qui dolorem eum fugiat quo voluptas nulla pariatur</p>
  </div>

  <svg class="divider-band" role="img" aria-label="Band of wireframe terrain" width="470" height="38" viewBox="0 0 470 38">
    <defs>
      <linearGradient id="bandFade" x1="0" y1="0" x2="1" y2="0">
        <stop offset="0" stop-color="#163457"/>
        <stop offset="1" stop-color="#2b5282"/>
      </linearGradient>
    </defs>
    <rect width="470" height="38" fill="url(#bandFade)"/>
  </svg>

  <div class="section section--scope">
    <h2>Project Scope</h2>
    <p>Sed ut perspiciatis unde omnis iste natus error sit voluptatem accusantium doloremque laudantium, totam rem aperiam, eaque ipsa quae ab illo inventore veritatis et quasi architecto beatae vitae dicta sunt explicabo. Nemo enim ipsam voluptatem quia voluptas sit aspernatur aut odit aut fugit, sed quia consequuntur magni dolores eos qui ratione voluptatem sequi nesciunt. Neque porro quisquam est, qui dolorem ipsum quia dolor sit amet, consectetur, adipisci velit, sed quia non numquam eius modi tempora incidunt ut labore et dolore magnam aliquam quaerat voluptatem. Ut enim ad minima veniam, quis nostrum exercitationem ullam corporis suscipit laboriosam, nisi ut aliquid ex ea commodi consequatur? Quis autem vel eum iure reprehenderit qui in ea voluptate velit esse quam nihil molestiae consequatur, vel illum qui dolorem eum fugiat quo voluptas nulla pariatur</p>
  </div>

  <footer class="footer">
    <div class="footer__cell">Page <b>2</b> of <b>2</b></div>
    <div class="footer__cell">Confidential</div>
    <div class="footer__cell">Job Number</div>
  </footer>
</section>

</body>
</html>
```